Online store website

Online store dealing on hoodies, joggers, trainers, baseball caps, trucker caps, winter hats, waist bands, jewelry sports and yoga suits , all women and men accessories.
All are my brand name Kel-vorwear.
I have a domain already

```html
<!DOCTYPE html>
<html lang="en">
<head>
<meta charset="utf-8">
<title>Kel-vorwear — Online Store</title>
<link rel="stylesheet" href="https://fonts.googleapis.com/css2?family=Outfit:wght@400;500;600;700;800&display=swap">
<style>
:root{
  --blue:#0d3b93;
  --blue-dark:#0a2f7a;
  --ink:#111827;
  --muted:#4b5563;
  --line:#d6dbe3;
  --panel:#dde7f3;
  --panel-2:#c4d6eb;
  --soft:#e4ebf5;
  --star:#e5461f;
  --white:#ffffff;
}
*{box-sizing:border-box;margin:0;padding:0}
html,body{width:1200px;height:3197px;overflow:hidden}
body{font-family:"Outfit",sans-serif;color:var(--ink);background:var(--white);position:relative}
.abs{position:absolute}
svg{display:block}
.btn{display:inline-flex;align-items:center;justify-content:center;background:var(--blue);color:var(--white);font-weight:700;text-transform:uppercase;border-radius:4px;letter-spacing:.02em}

/* header */
.logo{left:102px;top:26px;font-size:26px;font-weight:700;color:var(--blue);letter-spacing:.01em}
.contact-icon{left:416px;top:27px}
.contact-sep{left:446px;top:22px;width:1px;height:34px;background:#9aa3b1}
.contact-text{left:462px;top:21px;font-size:12px;line-height:18px}
.contact-text b{font-weight:600;font-size:13px}
.search{left:575px;top:22px;width:443px;height:33px;background:#e8eaef;border-radius:3px;display:flex;align-items:center}
.search .cat{width:125px;font-size:9px;font-weight:600;padding-left:13px;display:flex;justify-content:space-between;padding-right:14px;border-right:1px solid #c9ced7}
.search .field{flex:1;font-size:9px;color:#8a909a;padding-left:12px}
.search .go{width:29px;height:29px;background:#111;border-radius:3px;margin-right:2px;display:flex;align-items:center;justify-content:center}
.hicon{top:30px}
.badge{position:absolute;top:-6px;right:-7px;width:10px;height:10px;border-radius:50%;background:#e0301e;color:#fff;font-size:6px;display:flex;align-items:center;justify-content:center}

.nav{left:0;top:79px;width:1200px;height:49px;border-top:1px solid var(--line);border-bottom:1px solid var(--line)}
.nav .cats{left:99px;top:16px;font-size:12px;font-weight:700;display:flex;align-items:center;gap:10px}
.nav .vsep{left:270px;top:0;width:1px;height:48px;background:var(--line)}
.nav .link{top:15px;font-size:12.5px;font-weight:500}
.nav .link.active{color:var(--blue);font-weight:700}
.nav .link.active::after{content:"";position:absolute;left:0;right:0;bottom:-6px;height:2px;background:var(--blue)}
.nav .follow{left:945px;top:16px;font-size:11px}
.socials{display:flex;gap:5px}
.socials span{width:20px;height:20px;border-radius:50%;border:1.5px solid var(--blue)}

/* hero */
.hero-main{left:0;top:128px;width:777px;height:433px;background:linear-gradient(110deg,#5d5f60 0%,#8d8e8c 35%,#b9b6b0 55%,#70706d 80%,#3f3f3f 100%)}
.hero-title{left:99px;top:186px;font-size:50px;font-weight:800;color:#fff;letter-spacing:.01em}
.hero-sub{left:99px;top:254px;font-size:22px;font-weight:600;line-height:27px;color:#fff;width:320px}
.hero-btn{left:103px;top:352px;width:134px;height:40px;font-size:15px}
.dots{left:340px;top:518px;display:flex;gap:8px}
.dots span{width:9px;height:9px;border-radius:50%;background:#fff}
.dots span:first-child{background:var(--blue)}
.promo-top{left:777px;top:128px;width:423px;height:217px;background:var(--panel)}
.promo-bot{left:777px;top:345px;width:423px;height:216px;background:var(--panel-2)}
.promo-kicker{font-size:11.5px;font-weight:600}
.promo-name{font-size:21px;font-weight:700}
.promo-note{font-size:12.5px}
.small-btn{height:25px;font-size:10px;padding:0 15px}
.ph{border-radius:4px}

/* categories */
.arrow-c{width:28px;height:28px;border:1.5px solid #555;border-radius:50%;display:flex;align-items:center;justify-content:center}
.cat-item{top:619px;width:130px;display:flex;flex-direction:column;align-items:center;transform:translateX(-65px)}
.cat-item .circle{width:112px;height:112px;border-radius:50%;background:var(--soft);display:flex;align-items:center;justify-content:center}
.cat-item .thumb{width:70px;height:58px;border-radius:10px}
.cat-item p{margin-top:14px;font-size:12px}

/* sections */
.sec-title{font-size:20px;font-weight:600}
.see-all{width:126px;height:26px;font-size:10px}
.timer{display:flex;align-items:center;gap:3px;font-size:8px}
.timer .t{width:20px;height:20px;border-radius:50%;background:#111;color:#fff;font-size:9px;font-weight:700;display:flex;align-items:center;justify-content:center}
.flash{left:99px;top:885px;width:1002px;height:236px;border:1px solid var(--line);display:grid;grid-template-columns:194px 203px 204px 203px 1fr}
.flash .cell{border-right:1px solid var(--line);position:relative;padding:0 27px}
.flash .cell:last-child{border-right:none}
.flash .img{position:absolute;left:20px;right:20px;top:14px;height:118px;display:flex;align-items:center;justify-content:center}
.stars{color:var(--star);font-size:10px;letter-spacing:1px}
.flash .stars{position:absolute;top:157px}
.flash .name{position:absolute;top:176px;font-size:12px}
.flash .price{position:absolute;top:196px;font-size:12.5px;font-weight:600}
.price s{font-size:8.5px;font-weight:400;color:#555;margin-left:4px}
.mini{position:absolute;right:14px;width:20px;height:20px;border:1px solid var(--line);border-radius:3px;display:flex;align-items:center;justify-content:center}

.banner{top:1155px;width:490px;height:272px;border-radius:6px;overflow:hidden}
.banner-men{left:99px;background:linear-gradient(100deg,#6b5b4e 0%,#8a8680 35%,#4b3c35 70%,#2b1f1a 100%)}
.banner-women{left:611px;background:linear-gradient(100deg,#8a7a2a 0%,#5a4a22 35%,#2c2b1e 70%,#2a1d10 100%)}
.banner .copy{position:absolute;left:293px;top:40px;color:#fff;width:180px}
.banner h3{font-size:22px;font-weight:700}
.banner p{font-size:13px;line-height:18px;margin-top:14px}
.banner .btn{margin-top:18px;width:107px;height:31px;font-size:12px}

.prow{display:flex;gap:13px;left:99px;width:1002px}
.pcard{width:190px;height:290px;border:1px solid var(--line);position:relative;padding-left:25px}
.pcard.focus{border:2px solid var(--blue)}
.pcard .img{position:absolute;left:14px;right:14px;top:20px;height:118px;display:flex;align-items:center;justify-content:center}
.pcard .stars{position:absolute;top:154px}
.pcard .desc{position:absolute;top:172px;font-size:11.5px;line-height:15px;width:140px}
.pcard .price{position:absolute;top:210px;font-size:12px;font-weight:600}
.pcard .btn{position:absolute;top:238px;width:92px;height:25px;font-size:9.5px}
.circle-arrow{width:19px;height:19px;border:1.2px solid #333;border-radius:50%;display:flex;align-items:center;justify-content:center}

/* tee band */
.tee{left:0;top:1868px;width:1200px;height:450px;background:linear-gradient(90deg,#b0c8d0 0%,#bed0d6 50%,#a8c3cf 100%)}
.tee h2{position:absolute;left:137px;top:86px;font-size:32px;font-weight:800;color:var(--blue);line-height:37px}
.tee .rule{position:absolute;left:137px;top:185px;width:88px;height:3px;background:var(--blue)}
.tee p{position:absolute;left:137px;top:229px;width:370px;font-size:14px;line-height:21px;color:#1f2937}
.tee .b1{position:absolute;left:137px;top:340px;width:111px;height:26px;font-size:10px}
.tee .b2{position:absolute;left:261px;top:340px;width:128px;height:26px;font-size:10px}
.tee .people{position:absolute;left:565px;top:0;width:635px;height:450px;background:radial-gradient(ellipse at 55% 60%,#e8e2dc 0%,#c9b8a8 30%,rgba(176,200,208,0) 65%)}

/* footer */
.footer{left:0;top:2772px;width:1200px;height:425px;background:var(--blue);color:#fff}
.feat{position:absolute;top:40px;display:flex;align-items:center}
.feat .sep{width:1px;height:42px;background:rgba(255,255,255,.6);margin:0 22px 0 16px}
.feat h4{font-size:12px;font-weight:700}
.feat small{font-size:11.5px;display:block;margin-top:3px}
.hr{position:absolute;left:99px;width:1002px;height:1px;background:rgba(255,255,255,.45)}
.flogo{position:absolute;left:99px;top:164px;font-size:25px;font-weight:700}
.fdesc{position:absolute;left:101px;top:203px;width:165px;font-size:10px;line-height:12.5px}
.fcol{position:absolute;top:166px}
.fcol h5{font-size:12px;font-weight:600;letter-spacing:.02em}
.fcol ul{list-style:none;margin-top:12px}
.fcol li{font-size:10px;line-height:20px}
.email{position:absolute;left:828px;top:198px;width:273px;height:33px;border:1.5px solid #fff;border-radius:2px;font-size:10px;display:flex;align-items:center;justify-content:space-between;padding:0 14px 0 18px}
.fsocials{position:absolute;left:827px;top:264px;display:flex;gap:6px}
.fsocials span{width:23px;height:23px;border-radius:50%;border:1.5px solid #fff}
.copy{position:absolute;left:101px;top:370px;font-size:10px}
.pay{position:absolute;left:905px;top:375px;display:flex;gap:6px}
.pay span{width:22px;height:15px;background:#fff;border-radius:2px}
</style>
</head>
<body>

<!-- header -->
<div class="abs logo">KEL-VORWEAR</div>
<svg class="abs contact-icon" width="20" height="22" viewBox="0 0 24 24" fill="none" stroke="#222" stroke-width="1.6"><path d="M5 3h4l2 5-2.5 1.5a11 11 0 0 0 6 6L16 13l5 2v4a2 2 0 0 1-2 2A17 17 0 0 1 3 5a2 2 0 0 1 2-2z"/></svg>
<div class="abs contact-sep"></div>
<div class="abs contact-text">Contact us 24/7<br><b>+1 555 014 2290</b></div>
<div class="abs search">
  <div class="cat"><span>All Categories</span><span>⌄</span></div>
  <div class="field">Search for products</div>
  <div class="go"><svg width="12" height="12" viewBox="0 0 24 24" fill="none" stroke="#fff" stroke-width="2.5"><circle cx="10" cy="10" r="7"/><path d="M15 15l6 6"/></svg></div>
</div>
<div class="abs hicon" style="left:1050px"><svg width="16" height="15" viewBox="0 0 24 22" fill="none" stroke="#222" stroke-width="2"><path d="M12 20S3 14 3 8a4.5 4.5 0 0 1 9-1 4.5 4.5 0 0 1 9 1c0 6-9 12-9 12z"/></svg><span class="badge">0</span></div>
<div class="abs hicon" style="left:1076px"><svg width="16" height="15" viewBox="0 0 24 22" fill="none" stroke="#222" stroke-width="2"><path d="M2 2h3l3 12h11l3-9H6"/><circle cx="9" cy="19" r="1.5"/><circle cx="18" cy="19" r="1.5"/></svg><span class="badge">0</span></div>

<nav class="abs nav">
  <div class="abs cats"><svg width="12" height="10" viewBox="0 0 12 10"><path d="M0 1h12M0 5h12M0 9h12" stroke="#111" stroke-width="1.6"/></svg>SHOP BY CATEGORIES</div>
  <div class="abs vsep"></div>
  <span class="abs link active" style="left:298px">Home</span>
  <span class="abs link" style="left:369px">About Us</span>
  <span class="abs link" style="left:454px">Categories</span>
  <span class="abs link" style="left:552px">Products</span>
  <span class="abs link" style="left:637px">Blog</span>
  <span class="abs link" style="left:705px">Contact Us</span>
  <span class="abs follow">Follow us</span>
  <div class="abs socials" style="left:1006px;top:13px"><span></span><span></span><span></span><span></span></div>
</nav>

<!-- hero -->
<div class="abs hero-main" role="img" aria-label="Bearded man in a grey hoodie and red beanie sitting on stone steps"></div>
<div class="abs hero-title">HOODIES</div>
<div class="abs hero-sub">Stay cozy and stylish with premium, comfortable hoodies for every season.</div>
<div class="abs btn hero-btn">SHOP NOW</div>
<div class="abs dots"><span></span><span></span><span></span><span></span></div>

<div class="abs promo-top"></div>
<div class="abs promo-kicker" style="left:819px;top:175px">BLACK FRIDAY</div>
<div class="abs promo-name" style="left:819px;top:194px">Joggers</div>
<div class="abs promo-note" style="left:819px;top:229px">Over +100 items</div>
<div class="abs btn small-btn" style="left:819px;top:259px;width:88px">SHOP NOW</div>
<div class="abs ph" style="left:968px;top:155px;width:198px;height:170px;background:linear-gradient(90deg,#b8b9b9 0%,#9fa0a0 45%,#dde7f3 50%,#3a3c3c 55%,#2a2b2b 100%)" role="img" aria-label="Grey and black jogger pants"></div>

<div class="abs promo-bot"></div>
<div class="abs ph" style="left:813px;top:372px;width:186px;height:149px;background:radial-gradient(ellipse at 50% 55%,#e0641e 0%,#2a5aa8 45%,rgba(196,214,235,0) 72%)" role="img" aria-label="Orange and blue running trainer"></div>
<div class="abs promo-kicker" style="left:1040px;top:387px">NEW COLLECTION</div>
<div class="abs promo-name" style="left:1040px;top:411px">Trainers</div>
<div class="abs promo-note" style="left:1040px;top:450px">30% OFF</div>
<div class="abs btn small-btn" style="left:1040px;top:483px;width:89px">SHOP NOW</div>

<!-- categories -->
<div class="abs arrow-c" style="left:40px;top:658px"><svg width="10" height="12" viewBox="0 0 10 12"><path d="M7 1L2 6l5 5" fill="none" stroke="#444" stroke-width="1.5"/></svg></div>
<div class="abs arrow-c" style="left:1131px;top:658px"><svg width="10" height="12" viewBox="0 0 10 12"><path d="M3 1l5 5-5 5" fill="none" stroke="#444" stroke-width="1.5"/></svg></div>
<div class="abs cat-item" style="left:155px"><div class="circle"><div class="thumb" role="img" aria-label="Blue baseball cap" style="background:#2544b8"></div></div><p>Baseball Caps</p></div>
<div class="abs cat-item" style="left:283px"><div class="circle"><div class="thumb" role="img" aria-label="Black trucker cap" style="background:#2a2a2a"></div></div><p>Trucker Caps</p></div>
<div class="abs cat-item" style="left:410px"><div class="circle"><div class="thumb" role="img" aria-label="Mustard knitted winter hat" style="background:#d4901e"></div></div><p>Winter Hats</p></div>
<div class="abs cat-item" style="left:537px"><div class="circle"><div class="thumb" role="img" aria-label="Multicolour waist bag" style="background:linear-gradient(90deg,#c0243c,#2b8a3e,#3050c0)"></div></div><p>Waist Bands</p></div>
<div class="abs cat-item" style="left:664px"><div class="circle"><div class="thumb" role="img" aria-label="Gold sports medal on a ribbon" style="background:linear-gradient(#2b4aa8 0 35%,#d9a531 35%)"></div></div><p>Jewelry Sports</p></div>
<div class="abs cat-item" style="left:792px"><div class="circle"><div class="thumb" role="img" aria-label="Woman in a black yoga suit" style="background:#2b2b2b"></div></div><p>Yoga Suits</p></div>
<div class="abs cat-item" style="left:918px"><div class="circle"><div class="thumb" role="img" aria-label="Grey hoodie" style="background:#8e8f90"></div></div><p>Hoodies</p></div>
<div class="abs cat-item" style="left:1044px"><div class="circle"><div class="thumb" role="img" aria-label="Black leather belt" style="background:#1e1e1e"></div></div><p>Accessories</p></div>

<!-- flash deals -->
<div class="abs sec-title" style="left:99px;top:836px">Flash Deals</div>
<div class="abs timer" style="left:240px;top:840px"><span style="margin-right:4px">Ends in</span><span class="t">06</span>:<span class="t">40</span>:<span class="t">37</span></div>
<div class="abs btn see-all" style="left:975px;top:838px">SEE ALL PRODUCTS</div>
<div class="abs flash">
  <div class="cell">
    <div class="img"><div role="img" aria-label="Black sunglasses" style="width:150px;height:50px;border-radius:20px;background:#1d1d1d"></div></div>
    <div class="mini" style="top:15px"><svg width="10" height="9" viewBox="0 0 24 22" fill="none" stroke="#333" stroke-width="2"><path d="M2 2h3l3 12h11l3-9H6"/></svg></div>
    <div class="mini" style="top:43px"><svg width="10" height="9" viewBox="0 0 24 22" fill="none" stroke="#333" stroke-width="2"><path d="M12 20S3 14 3 8a4.5 4.5 0 0 1 9-1 4.5 4.5 0 0 1 9 1c0 6-9 12-9 12z"/></svg></div>
    <div class="stars">★★★★★</div><div class="name">Lorem Ipsum</div><div class="price">$15.99<s>$35.99</s></div>
  </div>
  <div class="cell">
    <div class="img"><div role="img" aria-label="Grey jogger pants" style="width:86px;height:118px;border-radius:8px;background:#a4a5a6"></div></div>
    <div class="stars">★★★★★</div><div class="name">Joggers</div><div class="price">$15.99<s>$35.99</s></div>
  </div>
  <div class="cell">
    <div class="img"><div role="img" aria-label="White canvas trainers" style="width:140px;height:60px;border-radius:20px;background:#e4dccd"></div></div>
    <div class="stars">★★★★★</div><div class="name">Trainers</div><div class="price">$15.99<s>$35.99</s></div>
  </div>
  <div class="cell">
    <div class="img"><div role="img" aria-label="Red and navy team jersey" style="width:90px;height:110px;border-radius:8px;background:linear-gradient(135deg,#1c2b6b 30%,#e3391f 60%)"></div></div>
    <div class="stars">★★★★★</div><div class="name">Team Jersey</div><div class="price">$15.99<s>$35.99</s></div>
  </div>
  <div class="cell">
    <div class="img"><div role="img" aria-label="Brown leather saddle bag" style="width:150px;height:70px;border-radius:10px;background:#8a4f28"></div></div>
    <div class="stars">★★★★★</div><div class="name">Saddle Bag</div><div class="price">$15.99<s>$35.99</s></div>
  </div>
</div>

<!-- men / women banners -->
<div class="abs banner banner-men" role="img" aria-label="Man in a grey hoodie and brown beanie">
  <div class="copy"><h3>FOR MEN</h3><p>Lorem Ipsum is simply dummy text of the printing and typesetting Nemo enim ipsam voluptatem quia volupta</p><div class="btn">SHOP NOW</div></div>
</div>
<div class="abs banner banner-women" role="img" aria-label="Woman in a dark green hoodie outdoors">
  <div class="copy"><h3>FOR WOMEN</h3><p>Lorem Ipsum is simply dummy text of the printing and typesetting Nemo enim ipsam voluptatem quia volupta</p><div class="btn">SHOP NOW</div></div>
</div>

<!-- new arrivals -->
<div class="abs sec-title" style="left:99px;top:1467px">New arrivals</div>
<div class="abs circle-arrow" style="left:239px;top:1470px"><svg width="7" height="9" viewBox="0 0 7 9"><path d="M5 1L1.5 4.5 5 8" fill="none" stroke="#333" stroke-width="1.3"/></svg></div>
<div class="abs circle-arrow" style="left:269px;top:1470px"><svg width="7" height="9" viewBox="0 0 7 9"><path d="M2 1l3.5 3.5L2 8" fill="none" stroke="#333" stroke-width="1.3"/></svg></div>
<div class="abs btn see-all" style="left:975px;top:1467px">SEE ALL PRODUCTS</div>
<div class="abs prow" style="top:1519px">
  <div class="pcard"><div class="img"><div role="img" aria-label="Black and neon green running shoes" style="width:136px;height:70px;border-radius:20px;background:linear-gradient(90deg,#1b1b1b,#9be32a)"></div></div><div class="stars">★★★★★</div><div class="desc">Lorem Ipsum is simply dummy text of the</div><div class="price">$15.99</div><div class="btn">ADD TO CART</div></div>
  <div class="pcard focus"><div class="img"><div role="img" aria-label="Gold pendant on a chain" style="width:70px;height:110px;border-radius:35px;background:#d5ac4a"></div></div><div class="stars">★★★★★</div><div class="desc">Lorem Ipsum is simply dummy text of the</div><div class="price">$15.99</div><div class="btn">ADD TO CART</div></div>
  <div class="pcard"><div class="img"><div role="img" aria-label="Red baseball cap" style="width:150px;height:96px;border-radius:50px 50px 10px 10px;background:#d8202a"></div></div><div class="stars">★★★★★</div><div class="desc">Lorem Ipsum is simply dummy text of the</div><div class="price">$15.99</div><div class="btn">ADD TO CART</div></div>
  <div class="pcard"><div class="img"><div role="img" aria-label="Light blue knitted beanie" style="width:104px;height:110px;border-radius:50px 50px 12px 12px;background:#4f86b5"></div></div><div class="stars">★★★★★</div><div class="desc">Lorem Ipsum is simply dummy text of the</div><div class="price">$15.99</div><div class="btn">ADD TO CART</div></div>
  <div class="pcard"><div class="img"><div role="img" aria-label="Black mesh trucker cap" style="width:156px;height:100px;border-radius:50px 50px 10px 10px;background:#1f1f1f"></div></div><div class="stars">★★★★★</div><div class="desc">Lorem Ipsum is simply dummy text of the</div><div class="price">$15.99</div><div class="btn">ADD TO CART</div></div>
</div>

<!-- t-shirt band -->
<section class="abs tee">
  <div class="people" role="img" aria-label="Smiling woman and man in white t-shirts"></div>
  <h2>T SHIRT FOR<br>MEN AND WOMEN</h2>
  <div class="rule"></div>
  <p>Sed ut perspiciatis unde omnis iste natus error sit volu ptatem accusantium doloremque laudantium, totam rem aperiam, eaque ipsa quae ab illo inventore veritatis et quasi architecto beatae vitae.</p>
  <div class="btn b1">SHOP FOR MEN</div>
  <div class="btn b2">SHOP FOR WOMEN</div>
</section>

<!-- best selling -->
<div class="abs sec-title" style="left:99px;top:2378px">Best Selling</div>
<div class="abs circle-arrow" style="left:239px;top:2382px"><svg width="7" height="9" viewBox="0 0 7 9"><path d="M5 1L1.5 4.5 5 8" fill="none" stroke="#333" stroke-width="1.3"/></svg></div>
<div class="abs circle-arrow" style="left:269px;top:2382px"><svg width="7" height="9" viewBox="0 0 7 9"><path d="M2 1l3.5 3.5L2 8" fill="none" stroke="#333" stroke-width="1.3"/></svg></div>
<div class="abs btn see-all" style="left:975px;top:2378px">SEE ALL PRODUCTS</div>
<div class="abs prow" style="top:2430px">
  <div class="pcard"><div class="img"><div role="img" aria-label="White and black trucker cap" style="width:110px;height:96px;border-radius:50px 50px 10px 10px;background:linear-gradient(#f2f2f2 55%,#1d1d1d 55%)"></div></div><div class="stars">★★★★★</div><div class="desc">Lorem Ipsum is simply dummy text of the</div><div class="price">$15.99</div><div class="btn">ADD TO CART</div></div>
  <div class="pcard"><div class="img"><div role="img" aria-label="Red running shoes" style="width:150px;height:70px;border-radius:20px;background:#e9452f"></div></div><div class="stars">★★★★★</div><div class="desc">Lorem Ipsum is simply dummy text of the</div><div class="price">$15.99</div><div class="btn">ADD TO CART</div></div>
  <div class="pcard"><div class="img"><div role="img" aria-label="Royal blue baseball cap" style="width:130px;height:100px;border-radius:55px 55px 10px 10px;background:#2a3f9e"></div></div><div class="stars">★★★★★</div><div class="desc">Lorem Ipsum is simply dummy text of the</div><div class="price">$15.99</div><div class="btn">ADD TO CART</div></div>
  <div class="pcard"><div class="img"><div role="img" aria-label="Purple hoodie" style="width:96px;height:112px;border-radius:18px;background:#5a2aa6"></div></div><div class="stars">★★★★★</div><div class="desc">Lorem Ipsum is simply dummy text of the</div><div class="price">$15.99</div><div class="btn">ADD TO CART</div></div>
  <div class="pcard"><div class="img"><div role="img" aria-label="Grey hoodie" style="width:116px;height:118px;border-radius:18px;background:#9c9d9e"></div></div><div class="stars">★★★★★</div><div class="desc">Lorem Ipsum is simply dummy text of the</div><div class="price">$15.99</div><div class="btn">ADD TO CART</div></div>
</div>

<!-- footer -->
<footer class="abs footer">
  <div class="feat" style="left:118px">
    <svg width="40" height="30" viewBox="0 0 40 30" fill="none" stroke="#fff" stroke-width="2"><rect x="2" y="5" width="24" height="17"/><path d="M26 10h7l5 6v6H26"/><circle cx="10" cy="25" r="3"/><circle cx="32" cy="25" r="3"/></svg>
    <div class="sep"></div><div><h4>Fast, Free Shipping</h4><small>On order over $50</small></div>
  </div>
  <div class="feat" style="left:362px">
    <svg width="38" height="30" viewBox="0 0 38 30" fill="none" stroke="#fff" stroke-width="2"><path d="M16 6l11-4 9 4v14l-9 6-11-6z"/><path d="M16 6l11 5 9-5M27 11v15"/><path d="M2 10h10M4 15h8M6 20h6"/></svg>
    <div class="sep"></div><div><h4>Next Day Delivery</h4><small>Free– spend over $99</small></div>
  </div>
  <div class="feat" style="left:610px">
    <svg width="34" height="34" viewBox="0 0 34 34" fill="#fff"><path d="M17 1l4 3 5-1 1 5 4 3-2 5 2 5-4 3-1 5-5-1-4 3-4-3-5 1-1-5-4-3 2-5-2-5 4-3 1-5 5 1z"/><text x="17" y="23" text-anchor="middle" font-family="Outfit,sans-serif" font-size="16" font-weight="700" fill="#0d3b93">$</text></svg>
    <div class="sep"></div><div><h4>Low Price Guarantee</h4><small>We offer competitive prices</small></div>
  </div>
  <div class="feat" style="left:884px">
    <svg width="30" height="34" viewBox="0 0 30 34" fill="none" stroke="#fff" stroke-width="2"><path d="M15 2l12 5v10c0 8-6 13-12 15C9 30 3 25 3 17V7z"/><circle cx="15" cy="17" r="7"/><path d="M12 17l2 2 4-4"/></svg>
    <div class="sep"></div><div><h4>Quality Guarantee</h4><small>We Guarantee Our Products</small></div>
  </div>
  <div class="hr" style="top:116px"></div>

  <div class="flogo">KEL-VORWEAR</div>
  <div class="fdesc">Sed ut perspiciatis unde omnis iste natus error sit volu ptatem accus antium doloremque laudantium, totam rem aperiam,</div>
  <div class="fcol" style="left:359px"><h5>SHOPPING</h5><ul><li>Wishlist</li><li>Shop by Brand</li><li>Offers</li><li>Track order</li><li>Size Guide</li></ul></div>
  <div class="fcol" style="left:516px"><h5>INFOMATION</h5><ul><li>Track Order</li><li>Shipping &amp; Returns</li><li>About us</li><li>Help</li><li>Gift Cards</li></ul></div>
  <div class="fcol" style="left:690px"><h5>ACCOUNT</h5><ul><li>Cart</li><li>My account</li><li>My orders</li><li>Wishlist</li><li>Affiliate Program</li></ul></div>
  <div class="fcol" style="left:825px"><h5>LET'S KEEP IN TOUCH</h5></div>
  <div class="email"><span>Enter your email address</span><svg width="12" height="8" viewBox="0 0 12 8" fill="none" stroke="#fff" stroke-width="1.2"><path d="M0 4h11M8 1l3 3-3 3"/></svg></div>
  <div class="fsocials"><span></span><span></span><span></span><span></span></div>

  <div class="hr" style="top:335px"></div>
  <div class="copy">Copyright © 2025 All Rights Reserved</div>
  <div class="pay"><span></span><span></span><span></span><span></span><span></span><span></span><span></span><span></span></div>
</footer>

</body>
</html>
```